Lumen Mobile Nutrition Funnel Pouch & Cap Pouch

The Funnel Pouch (without cap), Funnel Pouch (with cap), and Box will be using the same design and style, expect a few small changes for each.

Funnel Pouch (one time use)
1. Design for front and back of a Funnel Pouch & With Cap Funnel Pouch
2. Attached are the design requirements and photo of products

Funnel Pouch (Reusable)
3. this is the product WITH cap
4. the only difference in this design is that
"Spin n' Seal Cap" and "Reusable" need to be added somewhere on fron and back
- but overall it is the same design as the funnel pouch with no cap

After design is completed,
5. Professional white background image of both Funnel pouches

I have attached some examples of other products where you can get some ideas.
Updates

I am looking for a professional designer who I plan to work with long term for multiple projects. Please submit soon, thanks! Added Friday, April 7, 2017

Target Market(s)

health/ fitness enthusiasts, outdoor market, on the go indivudals, gym goers, Tallow Sports and Outdoors, Fernbrook Grocers

Industry/Entity Type

Supplement

Requirements
Must have
• Professional, creative design that follows basic requirements.
Nice to have
• incorporate LUMEN because that is our company logo name.
Should not have
• Should not be a design that I can easily make myself.

```html
<!DOCTYPE html>
<html lang="en">
<head>
<meta charset="utf-8">
<title>Lumen Mobile Nutrition – Funnel Pouch</title>
<link rel="stylesheet" href="https://fonts.googleapis.com/css2?family=Open+Sans:wght@300;600;700&display=swap">
<style>
  :root {
    --paper: #ffffff;
    --band-grey: #e6e7e8;
    --cocoa: #3c2415;
    --brand-red: #be1e2d;
    --logo-red: #ed1c24;
    --art-red: #a91a28;
    --ink-light: #ffffff;
  }
  html, body {
    margin: 0;
    padding: 0;
    width: 1200px;
    height: 2164px;
    overflow: hidden;
    background: var(--paper);
  }
  .pouch {
    position: relative;
    width: 1200px;
    height: 2164px;
    font-family: "Open Sans", Arial, sans-serif;
  }
  .pouch__shape,
  .usage-art {
    position: absolute;
    left: 0;
    top: 0;
    width: 1200px;
    height: 2164px;
  }
  .shape-grey { fill: var(--band-grey); }
  .shape-cocoa { fill: var(--cocoa); }
  .shape-red { fill: var(--brand-red); }
  .shape-arrow { fill: var(--ink-light); }
  .usage-art__area { fill: var(--art-red); }

  .brand-name {
    position: absolute;
    top: 50px;
    left: 0;
    width: 1200px;
    text-align: center;
    font-weight: 300;
    font-size: 205px;
    line-height: 1;
    letter-spacing: 66px;
    text-indent: 66px;
    color: var(--logo-red);
    margin: 0;
  }
  .tagline {
    position: absolute;
    top: 298px;
    left: 0;
    width: 1200px;
    text-align: center;
    font-weight: 600;
    font-size: 84px;
    line-height: 1.2;
    color: var(--ink-light);
    margin: 0;
  }
  .step {
    position: absolute;
    font-weight: 700;
    font-size: 64px;
    line-height: 75px;
    color: var(--ink-light);
    margin: 0;
  }
  .step--load {
    left: 176px;
    top: 752px;
  }
  .step--dispense {
    left: 374px;
    top: 1328px;
    width: 350px;
    text-align: center;
  }
</style>
</head>
<body>
  <main class="pouch">
    <svg class="pouch__shape" viewBox="0 0 722 1300" preserveAspectRatio="none" aria-hidden="true">
      <polygon class="shape-cocoa" points="0,0 722,0 470,1300 250,1300"/>
      <polygon class="shape-grey" points="0,0 722,0 688,175 34,175"/>
      <path class="shape-red" d="M48,252 C220,226 570,250 640,430 L500,1130 C330,1000 200,800 108,560 Z"/>
      <polygon class="shape-arrow" points="290,1160 432,1160 361,1300"/>
    </svg>

    <svg class="usage-art" viewBox="0 0 722 1300" preserveAspectRatio="none" role="img" aria-label="Line illustration: a scoop pours powder mix into the funnel pouch, which dispenses through its threaded tip into a drink bottle">
      <path class="usage-art__area" d="M305,325 H440 V430 H545 V690 H520 V1010 H440 V690 H405 V430 H305 Z"/>
    </svg>

    <h1 class="brand-name">LUMEN</h1>
    <p class="tagline">PORTABLE NUTRITION</p>

    <p class="step step--load">Load your Mix</p>
    <p class="step step--dispense">Dispense<br>Anytime<br>Into Any<br>Bottle</p>
  </main>
</body>
</html>
```